NorthPlain Bytes Yellow rose letterhead

I have a new logo for my company but in its current form it is too large to be used on letterhead or as a email signature. I need to have the designer use elements from the current logo and create something close to the original but more suited for smaller items.
Updates

I just uploaded a copy of our logo that does not have the weathered affect. Thanks

Industry/Entity Type

It Company

Requirements
Must have
• The design must maintain the visual effect of the current logo. It needs to include the yellow rose and the name of the company.
Nice to have
• It would be nice to maintain the stamp theme and incorporate my name, address, phone, email. etc.

```html
<!DOCTYPE html>
<html lang="en">
<head>
<meta charset="utf-8">
<title>NorthPlain Bytes Letterhead</title>
<link rel="stylesheet" href="https://fonts.googleapis.com/css2?family=Open+Sans:wght@400;700&display=swap">
<style>
  :root {
    --backdrop: #e9e7e4;
    --paper: #ffffff;
    --teal: #3cb6bb;
    --charcoal: #4a4542;
    --orange: #f0922b;
    --ink: #1e1e1e;
  }
  * { margin: 0; padding: 0; box-sizing: border-box; }
  html, body {
    width: 1054px;
    height: 1200px;
    overflow: hidden;
    background: var(--backdrop);
  }
  .letterhead {
    position: absolute;
    left: 132px;
    top: 42px;
    width: 790px;
    height: 1117px;
    background: var(--paper);
    box-shadow: 0 2px 10px rgba(0, 0, 0, 0.18);
    overflow: hidden;
    font-family: "Open Sans", sans-serif;
  }
  .header-swoosh,
  .footer-swoosh {
    position: absolute;
    left: 0;
    width: 790px;
  }
  .header-swoosh { top: 0; height: 200px; }
  .footer-swoosh { bottom: 0; height: 70px; }
  .brand {
    position: absolute;
    left: 43px;
    top: 92px;
    width: 184px;
    height: 140px;
    background: var(--paper);
    display: flex;
    align-items: center;
    gap: 12px;
    padding: 0 8px;
  }
  .brand-square {
    flex: none;
    width: 34px;
    height: 34px;
    background: var(--orange);
  }
  .brand-name {
    font-weight: 700;
    font-size: 23px;
    line-height: 1.15;
    color: var(--charcoal);
  }
  .sender {
    position: absolute;
    left: 464px;
    top: 22px;
    font-style: normal;
    color: var(--ink);
    font-size: 18px;
    line-height: 22.5px;
    letter-spacing: 0.2px;
  }
  .sender-name { font-size: 16px; }
</style>
</head>
<body>
  <main class="letterhead">
    <svg class="header-swoosh" viewBox="0 0 790 200" aria-hidden="true">
      <path d="M0,170 Q380,126 790,150 L790,168 Q380,146 0,184 Z" fill="var(--teal)"/>
    </svg>

    <div class="brand">
      <span class="brand-square"></span>
      <span class="brand-name">NorthPlain<br>Bytes</span>
    </div>

    <address class="sender">
      <div class="sender-name">Mara Lindqvist, PhD</div>
      <div>418 W Prairie Mesa Rd, Ste 210</div>
      <div>Hollis Creek, TX 75910</div>
      <div>1-800-555-0147</div>
      <div>mara@northplain-bytes.com</div>
    </address>

    <svg class="footer-swoosh" viewBox="0 0 790 70" aria-hidden="true">
      <defs>
        <linearGradient id="footer-fade" x1="0" y1="0" x2="1" y2="0">
          <stop offset="0" stop-color="var(--teal)"/>
          <stop offset="0.72" stop-color="var(--teal)"/>
          <stop offset="0.9" stop-color="var(--charcoal)"/>
          <stop offset="1" stop-color="var(--charcoal)"/>
        </linearGradient>
      </defs>
      <path d="M0,46 Q480,40 790,14 L790,70 L0,70 Z" fill="url(#footer-fade)"/>
    </svg>
  </main>
</body>
</html>
```